Design a single page Shopify store web page

We are looking to have a page designed for a single page Shopify store with 2 products. We already have a basic structure that we like, though we are open to suggestions. We are looking for somebody to provide a design/color scheme that we can then implement using Shopify's templating system. We can handle the implementation(HTML / CSS / jS) as we already have 2 web developers on the team, but have not been able to find a design we liked.

The job would consist of providing a mockup (photoshop or otherwise) and any vector graphics you choose to create for the site (we can provide product photos and other images).

You can also look at http://tidewrenco.com.au for some of our design direction we have used so far

Target Market(s)

Young Australian Males (18 - 49)

Industry/Entity Type

Store

Number of Pages Required

1 page

Font styles to use
Serif
Sans Serif

Requirements
Must have
• Single Page Design
• E-commerce Product Purchase
• Manly (whatever interpretation of that you have)

```html
<!DOCTYPE html>
<html lang="en">
<head>
<meta charset="utf-8">
<title>Plans</title>
<link rel="stylesheet" href="https://fonts.googleapis.com/css2?family=Amatic+SC:wght@700&family=Roboto:wght@100&family=Roboto+Slab:wght@300;400;700&display=swap">
<style>
  :root {
    --paper: #ffffff;
    --ink: #181c20;
    --heading: #ffffff;
    --plan-title: #b9bdc1;
    --muted: #7d8187;
    --feature-text: #ffffff;
    --price: rgba(72, 40, 138, 0.92);
    --cta: #33ab3a;
    --cta-text: #ffffff;
    --tick: #33ab3a;
    --photo-light: #f4f4f4;
    --photo-shade: #d6d6d6;
  }
  * { margin: 0; padding: 0; box-sizing: border-box; }
  html, body { width: 1200px; height: 772px; overflow: hidden; background: var(--paper); }
  .page { position: relative; width: 1200px; height: 772px; overflow: hidden; background: var(--paper); }
  .band { position: absolute; left: 0; top: 68px; width: 1200px; height: 668px; background: var(--ink); }
  .section-title {
    position: absolute; left: 0; width: 1234px; top: 84px; text-align: center;
    font-family: "Amatic SC", cursive; font-weight: 700; font-size: 68px;
    text-transform: uppercase; color: var(--heading); letter-spacing: 2px; line-height: 1;
  }
  .plan { position: absolute; top: 216px; width: 300px; text-align: center; }
  .plan--comfort { left: 72px; }
  .plan--style { left: 418px; }
  .plan-name {
    font-family: "Amatic SC", cursive; font-weight: 700; font-size: 54px;
    text-transform: uppercase; color: var(--plan-title); line-height: 1; letter-spacing: 0;
  }
  .plan-desc {
    margin-top: 10px; font-family: "Roboto Slab", Georgia, serif; font-weight: 300;
    font-size: 14px; line-height: 16px; color: var(--muted); letter-spacing: 0.9px;
  }
  .product-photo {
    position: absolute; top: 345px; width: 228px; height: 203px;
    background: linear-gradient(160deg, var(--photo-light), var(--photo-shade));
    border-radius: 10px 10px 6px 6px;
  }
  .product-photo--comfort { left: 108px; }
  .product-photo--style { left: 441px; }
  .price {
    position: absolute; top: 424px; width: 148px; height: 148px; border-radius: 50%;
    background: var(--price); color: #fff; display: flex; align-items: center; justify-content: center;
    font-family: "Roboto", sans-serif; font-weight: 100; font-size: 60px; letter-spacing: -1px;
  }
  .price--comfort { left: 248px; }
  .price--style { left: 580px; }
  .buy-button {
    position: absolute; top: 588px; width: 160px; height: 48px; border-radius: 7px;
    background: var(--cta); color: var(--cta-text); display: flex; align-items: center; justify-content: center;
    font-family: "Roboto Slab", Georgia, serif; font-weight: 700; font-size: 19px; text-decoration: none;
  }
  .buy-button--comfort { left: 149px; }
  .buy-button--style { left: 482px; }
  .features { position: absolute; left: 780px; top: 336px; list-style: none; width: 320px; }
  .feature { position: relative; padding-left: 36px; margin-bottom: 20px; min-height: 22px;
    font-family: "Roboto Slab", Georgia, serif; font-weight: 400; font-size: 14px; line-height: 15px;
    color: var(--feature-text); letter-spacing: 1px; padding-top: 6px; }
  .feature svg { position: absolute; left: 1px; top: 0; }
</style>
</head>
<body>
<main class="page">
  <div class="band" aria-hidden="true"></div>

  <h1 class="section-title">Plans</h1>

  <section class="plan plan--comfort">
    <h2 class="plan-name">Comfort</h2>
    <p class="plan-desc">Lorem ipsum dolor sit amet,<br>consectetuer adipiscing elit.</p>
  </section>
  <section class="plan plan--style">
    <h2 class="plan-name">Style</h2>
    <p class="plan-desc">Fusce lobortis lorem at ipsum<br>semper sagittis.</p>
  </section>

  <div class="product-photo product-photo--comfort" role="img" aria-label="Photo of white cotton boxer shorts"></div>
  <div class="product-photo product-photo--style" role="img" aria-label="Photo of white cotton boxer shorts"></div>

  <div class="price price--comfort">$30</div>
  <div class="price price--style">$45</div>

  <a class="buy-button buy-button--comfort" href="#">GET IT!</a>
  <a class="buy-button buy-button--style" href="#">GET IT!</a>

  <ul class="features">
    <li class="feature"><svg width="24" height="26" viewBox="0 0 24 26"><path d="M2,14 L6,11 L10,18 L19,1 L23,3 L11,25 L8,25 Z" fill="var(--tick)"/></svg>Vestibulum auctor dapibus</li>
    <li class="feature"><svg width="24" height="26" viewBox="0 0 24 26"><path d="M2,14 L6,11 L10,18 L19,1 L23,3 L11,25 L8,25 Z" fill="var(--tick)"/></svg>Nunc dignissim risus id metus</li>
    <li class="feature"><svg width="24" height="26" viewBox="0 0 24 26"><path d="M2,14 L6,11 L10,18 L19,1 L23,3 L11,25 L8,25 Z" fill="var(--tick)"/></svg>Cras ornare tristique elit</li>
    <li class="feature"><svg width="24" height="26" viewBox="0 0 24 26"><path d="M2,14 L6,11 L10,18 L19,1 L23,3 L11,25 L8,25 Z" fill="var(--tick)"/></svg>Integer vitae libero ac risus<br>egestas placerat</li>
  </ul>
</main>
</body>
</html>
```